Illustrations for a Project Management Concept

we need illustrations for 5 project management principles that make up a holistic approach to project management, without all the BS. if we extract all the methodology, system, tool and mumbo-jumbo out of project management, we end up with some essential principles that are simple to understand and use. It's likely that people who use them will not be traditional Project Management types.

I've mocked up something that looks very corporate based on a template, but this has the wrong tone; the wrong feeling. I'd like something "funky" and colorful that conveys "Action" within "Simplicity".

the PPT file with the dark-blue background is the "corporate" consulting type mockup. the PPT with the white background shows an idea I had for breaking out each of the 5 principles (only one shown) to make it larger, with some text in a callout.

In the final deliverable, I need to be able to both show all 5 on one diagram, as well as slicing the image to display each principle separately. i do not have editing capabilities for vector image formats, only image formats

Reason: there are a number of designers who have only just accepted the invitation. I want to give everyone a chance to submit.

```html
<!DOCTYPE html>
<html lang="en">
<head>
<meta charset="utf-8">
<title>Suppress Project Entropy, Selectively</title>
<link href="https://fonts.googleapis.com/css2?family=Jost:ital,wght@0,400;0,500;1,400&display=swap" rel="stylesheet">
<style>
  :root {
    --orange: #ff6600;
    --white: #ffffff;
    --mist: #f3f3f3;
    --coral: #f49391;
    --ink: #111111;
  }
  html, body {
    margin: 0;
    padding: 0;
    overflow: hidden;
  }
  .principle-card {
    position: relative;
    width: 1200px;
    height: 834px;
    background: var(--orange);
    overflow: hidden;
    font-family: "Jost", "Futura", sans-serif;
    color: var(--ink);
  }
  .principle-shapes {
    position: absolute;
    inset: 0;
  }
  .principle-title {
    position: absolute;
    left: 410px;
    top: 288px;
    margin: 0;
    font-size: 22px;
    font-weight: 400;
    font-style: italic;
    line-height: 30px;
    letter-spacing: 0.2px;
  }
  .principle-body {
    position: absolute;
    left: 318px;
    top: 342px;
    width: 620px;
    margin: 0;
    text-align: center;
    font-size: 19px;
    line-height: 24.5px;
    letter-spacing: 0.2px;
  }
  .principle-badge {
    position: absolute;
    left: 845px;
    top: 522px;
    width: 186px;
    height: 186px;
    display: flex;
    align-items: center;
    justify-content: center;
    text-align: center;
    font-size: 26px;
    line-height: 32px;
    font-weight: 400;
  }
</style>
</head>
<body>
  <main class="principle-card">
    <svg class="principle-shapes" width="1200" height="834" viewBox="0 0 1200 834" aria-hidden="true">
      <circle class="main-disc" cx="608" cy="400" r="330" fill="var(--white)"/>
      <circle class="inner-disc" cx="608" cy="400" r="200" fill="var(--mist)"/>
      <path class="title-ribbon" d="M398 282 H810 C850 282 880 318 894 367 C872 342 842 326 810 326 H398 Z" fill="var(--coral)"/>
      <circle class="badge-ring" cx="937" cy="614" r="105" fill="var(--white)"/>
      <circle class="badge-disc" cx="937" cy="614" r="93" fill="var(--coral)"/>
    </svg>

    <h1 class="principle-title">5. Suppress Project Entropy, Selectively</h1>

    <p class="principle-body">
      Trust the implementation and guidance of the first 4<br>
      project action principles to significantly reduce the entropy<br>
      in your project. For the remaining entropic events,<br>
      selectively invest time only where the result will materially<br>
      improve the achievement of project outcomes. Do not<br>
      attempt to implement comprehensive entropy control<br>
      processes.
    </p>

    <div class="principle-badge">Suppress<br>Entropy</div>
  </main>
</body>
</html>
```